HVAC company business card design

We need a business card design for a HVAC company. The design must look professional. Both sides will be used. The total data to be on the business card is
Name
Position
Email
Direct Phone/Moile Phone
Company Contacts /Address, Phone, Fax, web)
All data will be submit once the design is confirmed. For generic purposes use;
Emre Toksoy
Managing Director
+902324815263 (Mobile)
4712 Sokak No: 9 KBSE Yenikent IZMIR TURKEY
Tel: +902324815263 Fax : +902324815269
www.luvon.com.tr

Target Market(s)

HVAC

Industry/Entity Type

Business

Contact Information for Business Card

The total data to be on the business card is
Name
Position
Email
Direct Phone/Moile Phone
Emre Toksoy
Managing Director
+902324815263 (Mobile)
www.luvon.com.tr
The BC will use both sides of the card. The front will include the full logo and the details for the business card holder. The business card can be divided into vertical/horizontal or to a special shape. The common data like the company address/phone/fax should be indicated elsewehere. The back can contain some part or the whole logo and must contain the web address.

Font styles to use
Serif
Sans Serif

Colors
0355a3
cfdfed

Requirements
Should not have
• Please be careful with the fonts, it shouldnt be too small or too big and must not interfere with the logo fonts. If you need to use a curvy shape please do not use as the logo is already curvy or use the curves from the logo (if it looks good, otherwise forget it)
• We are not in favor of pictograms, only if they are perfect use them.

```html
<!DOCTYPE html>
<html lang="en">
<head>
<meta charset="utf-8">
<title>Luvon business card</title>
<link rel="stylesheet" href="https://fonts.googleapis.com/css2?family=Arimo:wght@400;700&display=swap">
<style>
  :root{
    --blue:#2f6fc0;
    --navy:#2d3c5e;
    --paper:#f7f7f7;
    --paper-edge:#e6e8eb;
    --backdrop:#d9d6d0;
    --ink-light:#ffffff;
  }
  *{margin:0;padding:0;box-sizing:border-box}
  html,body{width:1200px;height:1023px;overflow:hidden;background:var(--backdrop);font-family:"Arimo",Arial,sans-serif}
  .card{position:absolute;left:175px;width:850px;height:486px;background:linear-gradient(135deg,#ffffff,var(--paper) 60%,var(--paper-edge));overflow:hidden;box-shadow:0 6px 18px rgba(0,0,0,.25)}
  .card--front{top:17px}
  .card--back{top:520px}

  .card-shapes{position:absolute;inset:0}

  .brand{position:absolute;display:flex;align-items:center;gap:14px;color:var(--navy);font-weight:700;letter-spacing:2px;white-space:nowrap}
  .brand__dot{border-radius:50%;background:var(--blue);flex:none}
  .card--front .brand{left:60px;top:340px;font-size:58px}
  .card--front .brand__dot{width:44px;height:44px}
  .card--back .brand{left:50%;top:215px;transform:translate(-50%,-50%);font-size:92px;gap:22px}
  .card--back .brand__dot{width:72px;height:72px}

  .back-web{position:absolute;left:0;right:0;top:300px;text-align:center;color:var(--blue);font-size:24px;letter-spacing:1px}

  .holder{position:absolute;right:62px;top:30px;text-align:right;color:var(--ink-light)}
  .holder__name{font-size:26px;font-weight:400}
  .holder__role{font-size:17px;margin-top:4px}

  .contacts{position:absolute;right:50px;top:150px;list-style:none;color:var(--ink-light);font-size:17px;line-height:25px;text-align:right}
  .contacts li{display:flex;justify-content:flex-end;align-items:center;gap:10px}
  .contacts svg{width:15px;height:15px;flex:none}

  .address{position:absolute;left:410px;right:0;top:385px;height:52px;background:var(--navy);color:var(--ink-light);font-size:17px;display:flex;align-items:center;padding-left:26px;white-space:nowrap}
</style>
</head>
<body>

<section class="card card--front">
  <svg class="card-shapes" viewBox="0 0 850 486" aria-hidden="true">
    <polygon points="390,0 850,0 850,486 610,486 610,440 470,440 470,300 330,300 330,130 390,130" fill="var(--blue)"/>
    <rect x="345" y="0" width="45" height="130" fill="var(--navy)"/>
    <rect x="490" y="95" width="6" height="230" fill="var(--navy)"/>
    <rect x="0" y="462" width="610" height="24" fill="var(--navy)"/>
    <rect x="610" y="468" width="240" height="18" fill="var(--navy)" opacity=".85"/>
  </svg>

  <div class="brand"><span class="brand__dot"></span>LUVON</div>

  <div class="holder">
    <p class="holder__name">Emre Toksoy</p>
    <p class="holder__role">Managing Director</p>
  </div>

  <ul class="contacts">
    <li>+902324815263
      <svg viewBox="0 0 16 16"><rect x="4" y="1" width="8" height="14" rx="1.5" fill="none" stroke="#fff" stroke-width="1.5"/><circle cx="8" cy="12.5" r="1" fill="#fff"/></svg></li>
    <li>+902324815263
      <svg viewBox="0 0 16 16"><rect x="2" y="4" width="12" height="9" rx="1.5" fill="none" stroke="#fff" stroke-width="1.5"/><rect x="5" y="2" width="6" height="3" fill="#fff"/></svg></li>
    <li>+902324815269
      <svg viewBox="0 0 16 16"><rect x="2" y="6" width="12" height="8" rx="1" fill="none" stroke="#fff" stroke-width="1.5"/><rect x="5" y="2" width="6" height="5" fill="none" stroke="#fff" stroke-width="1.3"/></svg></li>
    <li>info@luvon.com.tr
      <svg viewBox="0 0 16 16"><rect x="1.5" y="3.5" width="13" height="9" fill="none" stroke="#fff" stroke-width="1.5"/><path d="M1.5 3.5 8 9l6.5-5.5" fill="none" stroke="#fff" stroke-width="1.5"/></svg></li>
    <li>www.luvon.com.tr
      <svg viewBox="0 0 16 16"><circle cx="8" cy="8" r="6.5" fill="none" stroke="#fff" stroke-width="1.5"/><ellipse cx="8" cy="8" rx="3" ry="6.5" fill="none" stroke="#fff" stroke-width="1.2"/><path d="M1.5 8h13" stroke="#fff" stroke-width="1.2"/></svg></li>
  </ul>

  <p class="address">4712 Sokak No: 9 KBSE Yenikent IZMIR TURKEY</p>
</section>

<section class="card card--back">
  <svg class="card-shapes" viewBox="0 0 850 486" aria-hidden="true">
    <rect x="0" y="462" width="400" height="24" fill="var(--navy)"/>
    <rect x="420" y="462" width="430" height="24" fill="var(--blue)"/>
  </svg>
  <div class="brand"><span class="brand__dot"></span>LUVON</div>
  <p class="back-web">www.luvon.com.tr</p>
</section>

</body>
</html>
```